Oil and Gas Exploration and Production company needs a business card design

We need a business card design using our logo and colors in the logo. We want a mainstream design.

```html
<!DOCTYPE html>
<html lang="en">
<head>
<meta charset="utf-8">
<title>Vela Oil &amp; Gas — Business Card</title>
<link rel="stylesheet" href="https://fonts.googleapis.com/css2?family=Montserrat:wght@600;700&display=swap">
<style>
  :root {
    --page-bg: #ffffff;
    --card-sand: #f4d8ad;
    --card-sand-light: #f7e0bb;
    --card-vein: #f0c88c;
    --ink-brown: #4a3b33;
    --accent-gold: #d9a23c;
    --divider: #5a4a42;
  }
  * { margin: 0; padding: 0; box-sizing: border-box; }
  html, body {
    width: 1200px;
    height: 1200px;
    overflow: hidden;
    background: var(--page-bg);
  }
  .canvas {
    position: relative;
    width: 1200px;
    height: 1200px;
  }
  .business-card {
    position: absolute;
    left: 100px;
    top: 318px;
    width: 1004px;
    height: 572px;
    overflow: hidden;
  }
  .card-texture {
    position: absolute;
    inset: 0;
    width: 100%;
    height: 100%;
  }
  .brand {
    position: absolute;
    left: 218px;
    top: 588px;
    display: flex;
    align-items: center;
    gap: 12px;
    transform: translateX(-100px) translateY(-318px);
  }
  .brand-dot {
    width: 26px;
    height: 26px;
    border-radius: 50%;
    background: var(--accent-gold);
    flex: none;
  }
  .brand-name {
    font-family: "Montserrat", sans-serif;
    font-weight: 700;
    font-size: 30px;
    color: var(--ink-brown);
    white-space: nowrap;
  }
  .divider {
    position: absolute;
    left: 500px;
    top: 156px;
    width: 3px;
    height: 270px;
    background: var(--divider);
  }
  .person {
    position: absolute;
    left: 618px;
    top: 148px;
    width: 196px;
    text-align: center;
    font-family: "Montserrat", sans-serif;
    color: var(--ink-brown);
  }
  .person-name {
    font-weight: 700;
    font-size: 37px;
    letter-spacing: 0.3em;
    line-height: 1;
    margin-right: -0.3em;
  }
  .person-role {
    font-weight: 700;
    font-size: 20px;
    letter-spacing: 0.16em;
    line-height: 1;
    margin-top: 4px;
  }
  .contact-list {
    position: absolute;
    left: 546px;
    top: 306px;
    list-style: none;
    font-family: "Montserrat", sans-serif;
    font-weight: 700;
    font-size: 28px;
    letter-spacing: 0.17em;
    color: var(--ink-brown);
  }
  .contact-item {
    line-height: 45px;
    white-space: nowrap;
  }
</style>
</head>
<body>
  <main class="canvas">
    <section class="business-card" aria-label="Business card">
      <svg class="card-texture" role="img" aria-label="Flowing sand-coloured marble texture" viewBox="0 0 1004 572" preserveAspectRatio="none">
        <defs>
          <linearGradient id="sandMarble" x1="0" y1="0" x2="1" y2="1">
            <stop offset="0" stop-color="var(--card-sand-light)"/>
            <stop offset="0.5" stop-color="var(--card-sand)"/>
            <stop offset="1" stop-color="var(--card-sand-light)"/>
          </linearGradient>
        </defs>
        <rect width="1004" height="572" fill="url(#sandMarble)"/>
      </svg>

      <div class="brand">
        <span class="brand-dot"></span>
        <span class="brand-name">Vela Oil &amp; Gas</span>
      </div>

      <div class="divider"></div>

      <div class="person">
        <p class="person-name">NAME</p>
        <p class="person-role">DIRECTOR</p>
      </div>

      <ul class="contact-list">
        <li class="contact-item">+12 3456 7890 123</li>
        <li class="contact-item">contact@yourbrand</li>
        <li class="contact-item">www.yourbrand</li>
      </ul>
    </section>
  </main>
</body>
</html>
```